Simple but elegant business card/logo design for exclusive beauty business

We need a logo designed for a new elegant and exclusive beauty business called "R". The logo itself should be a stylistic and custom design for the letter "R". We would like the business card to have the logo as the centrepiece on a clean background. Gold Logo on black background or silver on white background.

The business card details should be displayed centre of the card. Details are as follows:

Tamsin Earle
Facebook: /shinesoftlyr
Instagram: /shinesoftlyr

The words "Shine Softly" should also appear somewhere on the card.

Industry/Entity Type

Business

Logo Text

G

Requirements
Must have
• Design must be simple, clean and elegant
Should not have
• The design should not be cluttered

```html
<!DOCTYPE html>
<html lang="en">
<head>
<meta charset="utf-8">
<title>Shine Softly by R — Business Card</title>
<link href="https://fonts.googleapis.com/css2?family=Open+Sans:wght@400;600&display=swap" rel="stylesheet">
<style>
  :root {
    --backdrop: #e9e8e6;
    --card: #ffffff;
    --silver: #8c8c8c;
    --silver-dark: #6e6e6e;
    --silver-light: #b5b5b5;
    --ghost: #f1f1f1;
    --shadow: rgba(0, 0, 0, 0.12);
  }
  * { box-sizing: border-box; margin: 0; padding: 0; }
  html, body {
    width: 857px; height: 1200px; overflow: hidden;
    background: var(--backdrop);
    font-family: "Open Sans", Arial, sans-serif;
  }
  .canvas {
    width: 857px; height: 1200px;
    display: flex; flex-direction: column;
    align-items: center; justify-content: center; gap: 90px;
  }
  .card {
    position: relative;
    width: 700px; height: 400px;
    background: var(--card);
    box-shadow: 0 10px 30px var(--shadow);
    overflow: hidden;
  }

  /* Front */
  .brand {
    position: absolute; left: 70px; top: 150px;
    color: var(--silver);
    font-weight: 600; font-size: 30px; line-height: 1.1;
    letter-spacing: 0.5px;
  }
  .brand-mark { font-size: 64px; line-height: 1; display: block; margin-top: 4px; }
  .divider {
    position: absolute; left: 318px; top: 70px;
    width: 2px; height: 260px;
    background: linear-gradient(to bottom, transparent, var(--silver-light) 20%, var(--silver-dark) 80%, transparent);
  }
  .details {
    position: absolute; left: 350px; top: 118px;
    color: var(--silver-dark);
  }
  .name { font-size: 26px; font-weight: 400; color: var(--silver); margin-bottom: 14px; }
  .contact-list { list-style: none; }
  .contact-list li {
    display: flex; align-items: center; gap: 12px;
    font-size: 16px; line-height: 30px; font-weight: 600;
  }
  .icon { width: 16px; height: 16px; flex: none; }
  .icon-square { width: 14px; height: 14px; background: var(--silver); border-radius: 2px; flex: none; margin: 0 1px; }

  /* Back */
  .ghost-pattern {
    position: absolute; inset: 0;
    background: radial-gradient(ellipse at 40% 30%, var(--ghost), transparent 60%),
                radial-gradient(ellipse at 75% 75%, var(--ghost), transparent 55%);
  }
  .centre-mark {
    position: absolute; inset: 0;
    display: flex; align-items: center; justify-content: center;
    color: var(--silver); font-weight: 600; font-size: 120px;
  }
</style>
</head>
<body>
<main class="canvas">
  <section class="card card-front">
    <div class="brand">Shine Softly<br>by <span class="brand-mark">R</span></div>
    <div class="divider"></div>
    <div class="details">
      <p class="name">Tamsin Earle</p>
      <ul class="contact-list">
        <li>
          <svg class="icon" viewBox="0 0 16 16"><rect x="4" y="1" width="8" height="14" rx="1.5" fill="none" stroke="#8c8c8c" stroke-width="1.5"/><circle cx="8" cy="12.5" r="0.9" fill="#8c8c8c"/></svg>
          0400 218 675
        </li>
        <li>
          <svg class="icon" viewBox="0 0 16 16"><rect x="1" y="3" width="14" height="10" rx="1" fill="none" stroke="#8c8c8c" stroke-width="1.5"/><path d="M1.5 4 L8 9 L14.5 4" fill="none" stroke="#8c8c8c" stroke-width="1.5"/></svg>
          hello@shinesoftlyr.com
        </li>
        <li>
          <svg class="icon" viewBox="0 0 16 16"><circle cx="8" cy="8" r="6.5" fill="none" stroke="#8c8c8c" stroke-width="1.4"/><ellipse cx="8" cy="8" rx="3" ry="6.5" fill="none" stroke="#8c8c8c" stroke-width="1.2"/><line x1="1.5" y1="8" x2="14.5" y2="8" stroke="#8c8c8c" stroke-width="1.2"/></svg>
          www.shinesoftlyr.com
        </li>
        <li><span class="icon-square"></span>/shinesoftlyr</li>
        <li><span class="icon-square"></span>/shinesoftlyr</li>
      </ul>
    </div>
  </section>

  <section class="card card-back">
    <div class="ghost-pattern" role="img" aria-label="Faint oversized brand letters as background decoration"></div>
    <div class="centre-mark">R</div>
  </section>
</main>
</body>
</html>
```